Landing Page - #1 Social Media Training

I need a landing page where i'm going to sell the number one social media for small business package. Hopefully i can use this template for others.

The themes are in oranges.

See www.ravendupo.com

Its a dogs breakfast.

I need high end, good looking, kelo/fendrolix/logos.
Would love a wordpress design but i could slice it into one if it wasn't.

Need room for feature bullet points, a video preview, and text along the bottom... Want it in oranges and whites like the packaging with social media along the top... Side bar on the right for opt-in box, left side copy etc.

Target Market(s)

The audience is small and medium businesses.

Industry/Entity Type

Small Business

Requirements
Must have
• Opt-in
headline
footer

```html
<!DOCTYPE html>
<html lang="en">
<head>
<meta charset="utf-8">
<title>Ravendupo – Social Media &amp; Internet Marketing</title>
<link rel="stylesheet" href="https://fonts.googleapis.com/css2?family=Arimo:ital,wght@0,400;0,700;1,400&display=swap">
<style>
:root{
  --orange:#f7931e;
  --orange-deep:#f07c12;
  --orange-light:#fbb040;
  --orange-text:#f37a17;
  --ink:#222;
  --body:#444;
  --muted:#8a8a8a;
  --panel:#f0f0f0;
  --band:#e6e6e6;
  --rule:#c9c9c9;
  --dark:#1e1e1e;
  --white:#fff;
}
*{box-sizing:border-box;margin:0;padding:0}
html,body{width:1137px;height:1200px;overflow:hidden;background:var(--white)}
body{font-family:"Arimo",Arial,sans-serif;color:var(--ink);position:relative}
.abs{position:absolute}

/* hero */
.hero-bg{position:absolute;left:0;top:0;width:1137px;height:436px}
.brand{left:72px;top:38px;font-size:66px;font-weight:700;color:var(--orange-deep);letter-spacing:-1px}
.brand-tag{left:150px;top:120px;font-size:22px;color:#4a8a9a}

.nav{left:520px;top:27px;width:580px;height:53px;border-radius:6px;
  background:linear-gradient(#4a4a4a,#1b1b1b);display:flex;box-shadow:0 2px 3px rgba(0,0,0,.35)}
.nav a{flex:1;display:flex;align-items:center;justify-content:center;color:var(--white);
  text-decoration:none;font-size:16px;border-left:1px solid #555}
.nav a:first-child{border-left:0;color:var(--orange-light);flex:.8}
.nav a:nth-child(2){flex:1.25}

.affiliate h2{font-size:18px;font-weight:400;color:var(--ink);margin-bottom:12px}
.affiliate{left:18px;top:201px;width:452px}
.affiliate p{font-size:13px;line-height:23.5px;color:#5a3a10;text-align:justify}
.view-more{left:398px;top:307px;font-size:14px;color:var(--ink)}
.btn-dark{height:38px;border-radius:5px;background:linear-gradient(#4a4a4a,#141414);color:var(--white);
  font-size:19px;display:flex;align-items:center;padding-left:18px;gap:10px;box-shadow:0 2px 3px rgba(0,0,0,.35)}
.btn-blog{left:88px;top:371px;width:140px}
.btn-info{left:275px;top:371px;width:140px}

.video-title{left:564px;top:131px;font-size:18px;color:var(--ink)}
.video{left:564px;top:166px;width:375px;height:245px;background:#111;border-radius:4px;padding:8px}
.video-bar{height:20px;background:#3a3a3a;color:#eee;font-size:11px;line-height:20px;padding-left:10px;white-space:nowrap;overflow:hidden}
.video-screen{height:178px;background:linear-gradient(100deg,#3a3f4a 0 38%,#e9eef3 38% 100%);position:relative}
.play{position:absolute;left:162px;top:73px;width:40px;height:30px;background:rgba(20,20,20,.8);border-radius:5px}
.play::after{content:"";position:absolute;left:15px;top:8px;border-left:13px solid #fff;border-top:7px solid transparent;border-bottom:7px solid transparent}
.video-ctrl{height:22px;background:linear-gradient(#3c3c3c,#1c1c1c);color:#bbb;font-size:10px;line-height:22px;padding-left:66px}
.dots{left:977px;top:403px;display:flex;gap:9px}
.dots span{width:15px;height:15px;border-radius:50%;background:var(--dark)}
.dots span:first-child{background:var(--white);border:2px solid var(--dark)}

/* tagline */
.tagline{left:0;top:436px;width:1137px;height:80px;background:var(--band);display:flex;align-items:center;justify-content:center;
  font-size:25px;font-style:italic;color:var(--muted)}

/* about */
.portrait{left:17px;top:538px;width:146px;height:145px;border:3px solid #ddd;border-radius:5px;
  background:linear-gradient(120deg,#f39a3a 0 25%,#5a5f6a 25% 100%)}
.section-title{font-size:18px;color:var(--orange-text);font-weight:400}
.about-title{left:181px;top:544px}
.about-text{left:179px;top:578px;width:452px;font-size:13px;line-height:25.5px;color:var(--body);text-align:justify}

.features{left:18px;top:706px;width:608px;height:248px;background:var(--panel);border-radius:5px}
.features .section-title{position:absolute;left:23px;top:22px}
.features-lead{position:absolute;left:24px;top:64px;font-size:18px;font-weight:700;color:var(--muted)}
.list{list-style:none}
.list li{font-size:14px;color:var(--ink);height:32px;position:relative;padding-left:20px}
.list li::before{content:"";position:absolute;left:2px;top:4px;border-left:5px solid #333;border-top:4px solid transparent;border-bottom:4px solid transparent}
.feat-a{position:absolute;left:64px;top:108px}
.feat-b{position:absolute;left:340px;top:108px}

/* awards */
.awards-title{left:653px;top:544px}
.trophies{left:660px;top:580px;width:462px;height:115px;
  background:linear-gradient(90deg,#fff 0,#d8d8d8 10%,#fff 20%,#c9b28a 30%,#fff 42%,#f5f5f5 55%,#d0d0d0 66%,#fff 80%,#ccc 92%,#fff 100%)}
.awards-a{left:666px;top:728px}
.awards-b{left:916px;top:728px}
.awards-list li{font-size:13px;color:var(--body);height:30px;padding-left:16px}
.awards-list li::before{content:"›";position:absolute;left:0;top:-2px;font-size:15px;color:#333;border:0}

/* footer band */
.footer-band{left:0;top:978px;width:1137px;height:156px;background:var(--panel)}
.footer-head{font-size:18px;color:var(--ink)}
.divider{top:994px;width:2px;height:124px;background:var(--rule)}
.pay-badge{left:18px;top:1035px;width:74px;height:74px;border-radius:50%;background:radial-gradient(#f8e27a,#d9b23a);box-shadow:0 2px 3px rgba(0,0,0,.3)}
.cards{left:116px;top:1061px;display:flex;gap:3px}
.cards span{width:33px;height:22px;border:1px solid #999;background:var(--white);font-size:7.5px;font-weight:700;color:#333;display:flex;align-items:center;justify-content:center}
.social{left:342px;top:1058px;display:flex;gap:13px}
.social span{width:36px;height:36px;border-radius:50%;background:#3b5998;color:var(--white);font-size:7.5px;font-weight:700;display:flex;align-items:center;justify-content:center;box-shadow:0 1px 2px rgba(0,0,0,.35)}
.social span:nth-child(2){background:#33aadd}
.social span:nth-child(3){background:#1d5d9c}
.social span:nth-child(4){background:#333}
.social span:nth-child(5){background:#2c62b5}
.social span:nth-child(6){background:var(--orange)}
.field-label{font-size:13px;color:#333;text-align:right;width:120px}
.field{width:201px;height:36px;background:var(--white);border:1px solid #bbb}
.subscribe{left:1018px;top:1078px;width:99px;height:31px;background:linear-gradient(#555,#1a1a1a);color:var(--white);font-size:15px;display:flex;align-items:center;justify-content:center;box-shadow:0 2px 3px rgba(0,0,0,.3)}

/* bottom */
.bottom{left:0;top:1134px;width:1137px;height:66px;background:linear-gradient(90deg,var(--orange-deep),var(--orange) 50%,var(--orange-light));
  display:flex;align-items:center;justify-content:space-between;padding:0 25px 0 26px;font-size:12px;color:var(--ink)}
.bottom nav span{margin:0 10px}
</style>
</head>
<body>

<svg class="hero-bg" viewBox="0 0 1137 436" aria-hidden="true">
  <defs>
    <radialGradient id="heroGlow" cx="0.55" cy="0.55" r="0.7">
      <stop offset="0" stop-color="#fcb54a"/>
      <stop offset="1" stop-color="#f68c1c"/>
    </radialGradient>
  </defs>
  <rect width="1137" height="436" fill="url(#heroGlow)"/>
  <path d="M0 0H1137V104H530C475 104 455 112 430 140C405 168 385 175 340 175H0Z" fill="#fff"/>
</svg>

<div class="abs brand">Ravendupo</div>

<nav class="abs nav">
  <a href="#">Home</a>
  <a href="#">About Marcus Hale</a>
  <a href="#">Press Room</a>
  <a href="#">Contact Us</a>
</nav>

<section class="abs affiliate">
  <h2>Affiliate</h2>
  <p>"de Finibus Bonorum et Malorum" by Cicero are also reproduced in their exact original form, accompanied by English versions from the 1914 translation by H. Rackham.</p>
</section>
<div class="abs view-more">View more</div>
<div class="abs btn-dark btn-blog">›&nbsp; RVD Blog</div>
<div class="abs btn-dark btn-info">›&nbsp; RVD Info</div>

<div class="abs video-title">Product Demo Video</div>
<div class="abs video">
  <div class="video-bar">(RVD for SMB) Ravendupo Online - StartCamp 101 for...</div>
  <div class="video-screen" role="img" aria-label="Video still of the presenter beside a slide"><span class="play"></span></div>
  <div class="video-ctrl">0:00 / 6:38</div>
</div>
<div class="abs dots"><span></span><span></span><span></span><span></span><span></span><span></span></div>

<div class="abs tagline">Social Media &amp; Internet Marketing for Today's Small to Medium Business</div>

<div class="abs portrait" role="img" aria-label="Portrait photo of Marcus Hale"></div>
<h3 class="abs section-title about-title">About Marcus Hale</h3>
<p class="abs about-text">The standard chunk of Lorem Ipsum used since the 1500s is reproduced below for those interested. Sections 1.10.32 and 1.10.33 from "de Finibus Bonorum et Malorum" by Cicero are also reproduced in their exact original form, accompanied.</p>

<section class="abs features">
  <h3 class="section-title">Features</h3>
  <p class="features-lead">One easy system to help grow your business Online!</p>
  <ul class="list feat-a">
    <li>Search Engine Marketing</li>
    <li>Social Media Marketing</li>
    <li>Social Network Marketing</li>
    <li>Geo - Targeted Marketing</li>
  </ul>
  <ul class="list feat-b">
    <li>Applications</li>
    <li>Social Tools</li>
    <li>Community Development</li>
  </ul>
</section>

<h3 class="abs section-title awards-title">Awards the product has won</h3>
<div class="abs trophies" role="img" aria-label="Row of award trophies"></div>
<ul class="abs list awards-list awards-a">
  <li>2 Vella Awards</li>
  <li>4 Emberly Awards</li>
  <li>3 Dawley Awards</li>
  <li>1 Media Achievement Award</li>
  <li>2 AVX Awards</li>
  <li>1 DX Award</li>
  <li>2 Commendor Awards</li>
  <li>2 MarKit Awards</li>
</ul>
<ul class="abs list awards-list awards-b">
  <li>1 Horizen Award</li>
  <li>2 Teddy's (Arthur Rowan)</li>
  <li>1 Astra Award</li>
  <li>1 Hermon Creative Award</li>
  <li>1 Mercor Award</li>
  <li>1 Fenny Gold Award</li>
</ul>

<div class="abs footer-band"></div>
<h4 class="abs footer-head" style="left:23px;top:994px;font-weight:400">Payments:</h4>
<div class="abs pay-badge" role="img" aria-label="Verified payment badge"></div>
<div class="abs cards">
  <span>kelo</span><span>Dizko</span><span>fendrolix</span><span>Amplex</span><span>eCheck</span>
</div>
<div class="abs divider" style="left:321px"></div>
<h4 class="abs footer-head" style="left:342px;top:994px;font-weight:400">Connect with us:</h4>
<div class="abs social">
  <span>Frendly</span><span>Chirpo</span><span>Dugly</span><span>Gloo</span><span>Spazo</span><span>Feed</span>
</div>
<div class="abs divider" style="left:639px"></div>
<h4 class="abs footer-head" style="left:664px;top:994px;font-weight:400">News Letter</h4>
<div class="abs field-label" style="left:664px;top:1040px">Username :</div>
<div class="abs field" style="left:796px;top:1029px"></div>
<div class="abs field-label" style="left:658px;top:1087px">E- mail Address :</div>
<div class="abs field" style="left:796px;top:1076px"></div>
<div class="abs subscribe">Subscribe</div>

<footer class="abs bottom">
  <span>Copyright © 2011 www.ravendupo.com All rights reserved</span>
  <nav>Terms and conditions<span>|</span>Privacy policy</nav>
</footer>

</body>
</html>
```